Pediatric Dentist Business Card

I need a business card designed for a dentist who works exclusively with children.
We prefer designs that are out of ordiary that is fun and interesting to kids.

there is no logo since this is a dentists office. The name of the doctor is "Tavor Kesh" if you want to get creative with that.

Target Market(s)

Kids

Industry/Entity Type

Business

Contact Information for Business Card

Anythings that is creative

Colors

Designer to choose colors to be used in the design.

```html
<!DOCTYPE html>
<html lang="en">
<head>
<meta charset="UTF-8">
<title>Tavor Kesh – Kids Dentist Business Card</title>
<link href="https://fonts.googleapis.com/css2?family=Fredoka:wght@400;500;600&display=swap" rel="stylesheet">
<style>
  :root {
    --page-bg: #eef1f4;
    --blue-deep: #0f6fb4;
    --blue-mid: #1b86cc;
    --blue-light: #3ea3e0;
    --blue-pale: #8fd0f6;
    --ink-blue: #1a6fb5;
    --sunny-orange: #f7a21b;
    --leaf-green: #3cb043;
    --bubble-pink: #ff8fb3;
    --lemon: #ffd84a;
    --white: #ffffff;
    --shadow: rgba(20, 40, 70, 0.22);
  }
  html, body {
    margin: 0;
    padding: 0;
    width: 1166px;
    height: 1200px;
    overflow: hidden;
    background: var(--page-bg);
    font-family: "Fredoka", sans-serif;
  }
  .sheet {
    position: relative;
    width: 1166px;
    height: 1200px;
  }
  .card {
    position: absolute;
    left: 93px;
    width: 980px;
    height: 540px;
    border-radius: 28px;
    overflow: hidden;
    box-shadow: 0 14px 34px var(--shadow);
    background: var(--white);
  }
  .card--front { top: 40px; }
  .card--back { top: 620px; }
  .card__art {
    position: absolute;
    inset: 0;
    width: 100%;
    height: 100%;
  }
  .brand {
    position: absolute;
    left: 450px;
    top: 180px;
    width: 460px;
    display: flex;
    flex-direction: column;
    align-items: center;
    gap: 20px;
  }
  .brand__dot {
    width: 72px;
    height: 72px;
    border-radius: 50%;
    background: var(--sunny-orange);
  }
  .brand__name {
    margin: 0;
    font-size: 70px;
    font-weight: 600;
    color: var(--ink-blue);
    line-height: 1;
  }
  .brand__tagline {
    margin: 0;
    font-size: 24px;
    font-weight: 500;
    color: var(--leaf-green);
    letter-spacing: 1px;
  }
  .person {
    position: absolute;
    left: 66px;
    top: 130px;
    color: var(--white);
  }
  .person__name {
    margin: 0;
    font-size: 50px;
    font-weight: 600;
    color: var(--lemon);
    letter-spacing: 1px;
    line-height: 1.1;
  }
  .person__role {
    margin: 8px 0 0;
    font-size: 24px;
    font-weight: 400;
  }
  .contact {
    position: absolute;
    left: 66px;
    top: 370px;
    color: var(--white);
    font-size: 22px;
    font-weight: 400;
    list-style: none;
    margin: 0;
    padding: 0;
    display: grid;
    grid-template-columns: auto auto;
    column-gap: 40px;
    row-gap: 16px;
  }
  .contact__item {
    display: flex;
    align-items: center;
    gap: 12px;
  }
  .contact__item--web { grid-column: 1 / 3; }
  .contact__badge {
    width: 32px;
    height: 32px;
    border-radius: 50%;
    display: flex;
    align-items: center;
    justify-content: center;
    flex: none;
  }
  .contact__badge--phone { background: var(--sunny-orange); }
  .contact__badge--mail { background: var(--leaf-green); }
  .contact__badge--web { background: var(--bubble-pink); }
  .contact__icon {
    width: 18px;
    height: 18px;
    fill: var(--white);
  }
</style>
</head>
<body>
<main class="sheet">

  <section class="card card--front" aria-label="Card front">
    <svg class="card__art" viewBox="0 0 980 540" preserveAspectRatio="none" aria-hidden="true">
      <defs>
        <linearGradient id="frontBlue" x1="0" y1="0" x2="1" y2="1">
          <stop offset="0" stop-color="#2a93d6"/>
          <stop offset="1" stop-color="#0f6fb4"/>
        </linearGradient>
      </defs>
      <path d="M0 0 H395 C430 70 380 170 330 260 C280 350 300 460 250 540 H0 Z" fill="var(--blue-light)"/>
      <path d="M0 0 H355 C390 70 340 170 290 260 C240 350 260 460 210 540 H0 Z" fill="url(#frontBlue)"/>
      <circle cx="140" cy="170" r="78" fill="#ffffff" opacity="0.1"/>
      <circle cx="70" cy="420" r="26" fill="var(--lemon)" opacity="0.9"/>
      <circle cx="200" cy="360" r="14" fill="var(--bubble-pink)"/>
      <circle cx="260" cy="80" r="18" fill="var(--leaf-green)"/>
      <circle cx="120" cy="60" r="9" fill="#ffffff" opacity="0.7"/>
      <circle cx="230" cy="470" r="10" fill="#ffffff" opacity="0.6"/>
      <circle cx="900" cy="70" r="22" fill="var(--lemon)"/>
      <circle cx="850" cy="470" r="16" fill="var(--bubble-pink)"/>
      <circle cx="560" cy="480" r="11" fill="var(--leaf-green)"/>
      <circle cx="600" cy="70" r="8" fill="var(--blue-light)"/>
      <path d="M560 420 q30 -22 60 0 t60 0 t60 0 t60 0" fill="none" stroke="var(--blue-pale)" stroke-width="6" stroke-linecap="round"/>
    </svg>
    <div class="brand">
      <span class="brand__dot"></span>
      <h1 class="brand__name">Tavor Kesh</h1>
      <p class="brand__tagline">Happy Smiles for Kids</p>
    </div>
  </section>

  <section class="card card--back" aria-label="Card back">
    <svg class="card__art" viewBox="0 0 980 540" preserveAspectRatio="none" aria-hidden="true">
      <defs>
        <linearGradient id="backBlue" x1="0" y1="0" x2="1" y2="1">
          <stop offset="0" stop-color="#2a93d6"/>
          <stop offset="1" stop-color="#1478bd"/>
        </linearGradient>
      </defs>
      <rect width="980" height="540" fill="url(#backBlue)"/>
      <path d="M760 0 H980 V540 H900 C880 450 860 360 820 280 C780 200 730 100 760 0 Z" fill="var(--blue-light)"/>
      <path d="M800 0 H980 V540 H935 C915 450 895 360 855 280 C815 200 770 100 800 0 Z" fill="var(--blue-deep)"/>
      <circle cx="640" cy="190" r="80" fill="#ffffff" opacity="0.1"/>
      <circle cx="900" cy="110" r="26" fill="var(--lemon)"/>
      <circle cx="940" cy="300" r="14" fill="var(--bubble-pink)"/>
      <circle cx="880" cy="450" r="18" fill="var(--sunny-orange)"/>
      <circle cx="720" cy="440" r="12" fill="var(--leaf-green)"/>
      <circle cx="560" cy="60" r="10" fill="#ffffff" opacity="0.6"/>
      <circle cx="500" cy="300" r="7" fill="#ffffff" opacity="0.5"/>
      <path d="M66 300 q20 -16 40 0 t40 0 t40 0 t40 0" fill="none" stroke="var(--blue-pale)" stroke-width="5" stroke-linecap="round"/>
    </svg>
    <div class="person">
      <h2 class="person__name">NAME TITLE</h2>
      <p class="person__role">Designation</p>
    </div>
    <ul class="contact">
      <li class="contact__item">
        <span class="contact__badge contact__badge--phone">
          <svg class="contact__icon" viewBox="0 0 24 24" aria-hidden="true"><path d="M6.6 10.8a15.1 15.1 0 0 0 6.6 6.6l2.2-2.2a1 1 0 0 1 1-.25 11.4 11.4 0 0 0 3.6.57 1 1 0 0 1 1 1V20a1 1 0 0 1-1 1A17 17 0 0 1 3 4a1 1 0 0 1 1-1h3.5a1 1 0 0 1 1 1c0 1.25.2 2.45.57 3.6a1 1 0 0 1-.25 1z"/></svg>
        </span>
        <span>0000 0000 00</span>
      </li>
      <li class="contact__item">
        <span class="contact__badge contact__badge--mail">
          <svg class="contact__icon" viewBox="0 0 24 24" aria-hidden="true"><path d="M3 5h18a1 1 0 0 1 1 1v12a1 1 0 0 1-1 1H3a1 1 0 0 1-1-1V6a1 1 0 0 1 1-1zm9 7 8.5-5.5h-17z"/></svg>
        </span>
        <span>hello@tavorkesh.test</span>
      </li>
      <li class="contact__item contact__item--web">
        <span class="contact__badge contact__badge--web">
          <svg class="contact__icon" viewBox="0 0 24 24" aria-hidden="true"><path d="M12 3a9 9 0 1 0 0 18 9 9 0 0 0 0-18zm0 2c1 1.2 1.8 3 2.1 5H9.9c.3-2 1.1-3.8 2.1-5zm-2.1 7h4.2c-.3 2-1.1 3.8-2.1 5-1-1.2-1.8-3-2.1-5z"/></svg>
        </span>
        <span>www.tavorkesh.test</span>
      </li>
    </ul>
  </section>

</main>
</body>
</html>
```